Mental Health

KVR HAVEN
Behavioral Health
4172 E. Dorrel St. Mesa, AZ 85217
Marguerite (480)555-0142 / Ivan 480-555-0187

Email: KVRHaven@Qortamail.com
Newly Remodeled & Spacious
g Staff
Registered Nurses
Licensed Independent &
Professional Substance &
Abuse Counselors
Behavioral Health Techs
Certified Caregivers
Behavioral Health &
Substance Abuse Professionals

To Refer a Patient
About Us
KVR Haven is a Fully Staffed Behavioral
Health Residential Facility, providing
treatment plans for adults suffering
with various Behavioral Health and
Substance Abuse disorders, while living
in a nice safe, clean and supportive
environment. Our home offers clients the
ability to learn the necessary skills to
help clients adapt, build self confidence
as well as independence, with the goal
of reducing the probability of a future
crisis or possible relapse. We offer
counseling programs, consisting of a
variety of addiction and recovery support
groups, independent living, coping and
social skills groups, as well as assisting
clients with using tools to create a resume
to help obtain employment and so much
more. We are committed to teaching
self management care and allowing
clients to understand how to utilize the
resources, skills and tools available for
long term success by providing superior
quality, all-inclusive living arrangements
and treatment options.

Thank you for your patience while I update the final content needed for us to make the final decision this week.

```html
<!DOCTYPE html>
<html lang="en">
<head>
<meta charset="UTF-8">
<title>KVR Haven Business Card</title>
<link href="https://fonts.googleapis.com/css2?family=Roboto:wght@300;400;500;700&display=swap" rel="stylesheet">
<style>
  :root {
    --bg: #6b6b6b;
    --card-white: #ffffff;
    --brand-blue: #1565c0;
    --brand-green: #6aab2a;
    --text-gray: #444444;
    --back-blue: #0a63c4;
    --back-blue-dark: #0557b0;
    --band-orange: #f26b21;
    --band-yellow: #f7a823;
    --band-red: #d0101b;
    --band-pink: #e2398f;
    --band-purple: #4a2587;
    --band-green: #74ad2a;
    --band-blue: #1565c0;
  }
  * { box-sizing: border-box; margin: 0; padding: 0; }
  html, body { width: 1200px; height: 800px; overflow: hidden; }
  body {
    background: var(--bg);
    font-family: 'Roboto', Arial, sans-serif;
    display: flex;
    align-items: center;
    justify-content: center;
    gap: 40px;
  }
  .card {
    width: 540px;
    height: 310px;
    border-radius: 18px;
    overflow: hidden;
    position: relative;
  }
  /* Front */
  .card-front { background: var(--card-white); }
  .brand {
    position: absolute;
    left: 40px;
    top: 120px;
    width: 240px;
    display: flex;
    align-items: center;
    gap: 12px;
  }
  .brand-dot {
    flex: none;
    width: 46px; height: 46px; border-radius: 50%;
    background: var(--brand-blue);
  }
  .brand-name {
    font-size: 28px;
    font-weight: 400;
    color: var(--brand-blue);
    letter-spacing: 1px;
    white-space: nowrap;
  }
  .contact {
    position: absolute;
    left: 308px;
    top: 62px;
    width: 220px;
    line-height: 1.25;
  }
  .contact-name { font-size: 15px; font-weight: 700; color: var(--brand-blue); text-transform: uppercase; }
  .contact-phone { font-size: 14px; color: var(--brand-green); margin-bottom: 6px; }
  .contact-company { font-size: 13px; color: var(--brand-blue); margin-top: 4px; }
  .contact-line { font-size: 12px; color: var(--text-gray); white-space: nowrap; }
  .color-band {
    position: absolute;
    left: 0; right: 0; bottom: 0;
    height: 9px;
    display: flex;
  }
  .color-band span { flex: 1; }
  .band-orange { background: var(--band-orange); }
  .band-yellow { background: var(--band-yellow); }
  .band-red { background: var(--band-red); }
  .band-pink { background: var(--band-pink); }
  .band-purple { background: var(--band-purple); }
  .band-green { background: var(--band-green); }
  .band-blue { background: var(--band-blue); }
  /* Back */
  .card-back {
    background: linear-gradient(160deg, var(--back-blue), var(--back-blue-dark));
    color: #ffffff;
    display: flex;
    flex-direction: column;
    align-items: center;
  }
  .back-brand {
    margin-top: 48px;
    display: flex;
    flex-direction: column;
    align-items: center;
    gap: 12px;
  }
  .back-brand-dot {
    width: 110px; height: 110px; border-radius: 50%;
    background: #1d8fe0;
  }
  .back-brand-name { font-size: 20px; font-weight: 400; color: #ffffff; letter-spacing: 1px; }
  .services {
    margin-top: 18px;
    text-align: center;
    font-size: 12.5px;
    line-height: 1.4;
  }
  .tick { vertical-align: -2px; margin: 0 3px; }
</style>
</head>
<body>
  <section class="card card-front">
    <div class="brand">
      <div class="brand-dot"></div>
      <div class="brand-name">KVR HAVEN</div>
    </div>
    <div class="contact">
      <div class="contact-name">Marguerite</div>
      <div class="contact-phone">(480)555-0142</div>
      <div class="contact-name">Ivan</div>
      <div class="contact-phone">480-555-0187</div>
      <div class="contact-company">KVR HAVEN Behavioral Health</div>
      <div class="contact-line">4172 E. Dorrel St. Mesa, AZ 85217</div>
      <div class="contact-line">KVRHaven@Qortamail.com</div>
    </div>
    <div class="color-band">
      <span class="band-orange"></span><span class="band-yellow"></span><span class="band-red"></span><span class="band-pink"></span><span class="band-purple"></span><span class="band-green"></span><span class="band-blue"></span>
    </div>
  </section>

  <section class="card card-back">
    <div class="back-brand">
      <div class="back-brand-dot"></div>
      <div class="back-brand-name">KVR HAVEN</div>
    </div>
    <p class="services">
      Newly Remodeled &amp; Spacious Staff Registered Nurses<br>
      Licensed Independent &amp; Professional Substance &amp; Abuse Counselors<br>
      Behavioral Health Techs
      <svg class="tick" width="13" height="13" viewBox="0 0 14 14" aria-hidden="true"><circle cx="7" cy="7" r="7" fill="#fff"/><path d="M3.8 7.2l2.2 2.2 4.2-4.4" stroke="#0a63c4" stroke-width="1.8" fill="none"/></svg>
      Certified Caregivers<br>
      Behavioral Health &amp; Substance Abuse Professionals
    </p>
  </section>
</body>
</html>
```